Event Center Website

We need a new website design for an upscale event center in Reno, Nevada. The building hosts everything from weddings to corporate events to funerals and it competitively more expensive. The overall look and feel is consistent with a Lake Tahoe aesthetic. The current site can be viewed at www.thefernlodgeva.com. They are looking for a major upgrade. A sample site they like is www.quillmarshlodge.com. We have new photography available (some attached). The site should be very visual. A site map is attached as well for direction on what elements the site should include as well as labels for navigation. I am looking for a home page and sample interior page. Any questions, let me know. Thanks.
Updates

I have added some photography of the center itself for use rather than stock photography. Thanks!

Target Market(s)

Brides, professionals, high-income

Industry/Entity Type

Building

Requirements
Must have
• See site map

```html
<!DOCTYPE html>
<html lang="en">
<head>
<meta charset="utf-8">
<title>Fernhollow – Events Center</title>
<link rel="stylesheet" href="https://fonts.googleapis.com/css2?family=Questrial&display=swap">
<style>
:root{
  --brown-dark:#553d2d;
  --brown:#6e5444;
  --brown-mid:#8a6c58;
  --footer-bar:#4a3b32;
  --text:#8a8480;
  --heading:#6a4c38;
  --link-blue:#2a6fc9;
  --white:#ffffff;
  --field:rgba(255,255,255,.28);
}
*{margin:0;padding:0;box-sizing:border-box}
html,body{width:856px;height:1200px;overflow:hidden;background:#fff}
body{font-family:"Questrial",sans-serif;position:relative;color:var(--text)}
h1,h2{font-weight:400}
.page{position:relative;width:856px;height:1200px}
.abs{position:absolute}

/* header */
.site-header{left:0;top:0;width:856px;height:131px;
  background:
    radial-gradient(ellipse 260px 90px at 300px 20px,rgba(90,66,50,.35),transparent 70%),
    radial-gradient(ellipse 200px 80px at 620px 60px,rgba(90,66,50,.3),transparent 70%),
    radial-gradient(ellipse 160px 70px at 80px 110px,rgba(90,66,50,.25),transparent 70%),
    linear-gradient(180deg,#8d6f5b 0%,#9c7d68 45%,#7d604d 100%)}
.brand{left:41px;top:36px;width:134px;height:43px;display:flex;align-items:center;justify-content:center;gap:8px;background:var(--brown-dark);color:#fff}
.brand-square{width:8px;height:8px;background:#fff}
.brand-name{font-size:17px;letter-spacing:.6px;line-height:1}
.search{left:669px;top:38px;width:142px;height:16px;border-radius:8px;background:#e4e1de}
.search svg{position:absolute;right:6px;top:2px}
.main-nav{left:0;top:114px;width:856px;height:18px}
.main-nav a{position:absolute;top:0;color:#fff;font-size:8px;text-decoration:none;white-space:nowrap}
.main-nav a.active::after{content:"";position:absolute;left:-9px;right:-9px;top:11px;height:3px;background:#fff}

/* hero */
.hero{left:0;top:131px;width:856px;height:261px;
  background:
    radial-gradient(ellipse 240px 120px at 420px 170px,rgba(150,90,40,.75),transparent 70%),
    radial-gradient(ellipse 300px 80px at 300px 160px,rgba(95,80,70,.7),transparent 70%),
    radial-gradient(ellipse 180px 90px at 80px 230px,rgba(70,110,50,.7),transparent 70%),
    radial-gradient(ellipse 180px 90px at 800px 220px,rgba(70,110,50,.7),transparent 70%),
    linear-gradient(180deg,#1f5fc0 0%,#4f8ad6 35%,#9a7550 62%,#7d6a52 85%,#5e6a3e 100%)}
.hero-arrow{top:118px;width:26px;height:26px}

/* welcome */
.section-title{width:856px;left:0;text-align:center;color:var(--heading);font-size:15px;letter-spacing:.3px}
.welcome-text{left:50px;top:440px;width:756px;text-align:center;font-size:11px;line-height:23.5px}
.btn{left:390px;top:529px;width:76px;height:28px;background:var(--brown);color:#fff;font-size:11.5px;display:flex;align-items:center;justify-content:center;border:1px solid #4d382a}

/* events */
.event-photo{top:627px;width:174px;height:95px}
.dot{top:744px;width:8px;height:8px;border-radius:50%}

/* menu & testimonials */
.block-title{font-size:15.5px;color:var(--heading);letter-spacing:.3px}
.rule{height:1px;background:var(--brown-mid)}
.menu-photo{top:833px;width:160px;height:94px}
.menu-text{top:937px;width:170px;font-size:11px;line-height:15px}
.avatar{top:835px;width:64px;height:64px;border-radius:50%}
.quote{top:906px;width:120px;font-size:11px;line-height:14.7px}
.quote-date{top:957px;font-size:8.5px;color:var(--link-blue)}

/* footer */
.site-footer{left:0;top:1016px;width:856px;height:146px;
  background:
    radial-gradient(ellipse 200px 70px at 420px 120px,rgba(120,95,80,.35),transparent 70%),
    radial-gradient(ellipse 220px 80px at 120px 30px,rgba(120,95,80,.3),transparent 70%),
    linear-gradient(180deg,#6a5547,#55443a)}
.footer-col{top:1032px;font-size:8px;line-height:13px;color:#e8e0d8;list-style:none}
.footer-col .sub{padding-left:12px;font-size:6px;color:#a8978a}
.field{border-radius:7px;background:var(--field);font-size:5.5px;color:#f0e8e0;padding:2px 10px}
.social{top:1032px;width:20px;height:20px;border-radius:50%}
.footer-bar{left:0;top:1162px;width:856px;height:38px;background:var(--footer-bar);color:#d8cec6;font-size:8px;text-align:center;line-height:38px}
</style>
</head>
<body>
<div class="page">

  <header class="site-header abs" role="img" aria-label="Warm brown header backdrop with soft leaf shadows"></header>

  <div class="brand abs">
    <span class="brand-square"></span>
    <span class="brand-name">Fernhollow</span>
  </div>

  <div class="search abs">
    <svg width="11" height="11" viewBox="0 0 11 11"><circle cx="4.5" cy="4.5" r="3.3" fill="none" stroke="#888" stroke-width="1.2"/><line x1="7" y1="7" x2="10" y2="10" stroke="#888" stroke-width="1.4"/></svg>
  </div>

  <nav class="main-nav abs">
    <a class="active" style="left:40px">HOME</a>
    <a style="left:85px">ABOUT US</a>
    <a style="left:145px">GALLERY</a>
    <a style="left:201px">WEDDINGS</a>
    <a style="left:264px">MEETINGS</a>
    <a style="left:326px">OTHER EVENTS</a>
    <a style="left:405px">CATERING</a>
    <a style="left:464px">MENUS</a>
    <a style="left:513px">FAQs</a>
    <a style="left:556px">TESTIMONIALS</a>
    <a style="left:635px">CONTACT US</a>
    <a style="left:707px">SCHEDULE AN APPOINTMENT</a>
  </nav>

  <section class="hero abs" role="img" aria-label="Photo of the timber-framed lodge event center under a blue sky">
    <svg class="hero-arrow abs" style="left:44px" viewBox="0 0 26 26"><circle cx="13" cy="13" r="12" fill="none" stroke="#fff" stroke-width="1.3"/><polyline points="15,7 9,13 15,19" fill="none" stroke="#fff" stroke-width="1.3"/></svg>
    <svg class="hero-arrow abs" style="left:786px" viewBox="0 0 26 26"><circle cx="13" cy="13" r="12" fill="none" stroke="#fff" stroke-width="1.3"/><polyline points="11,7 17,13 11,19" fill="none" stroke="#fff" stroke-width="1.3"/></svg>
  </section>

  <h1 class="section-title abs" style="top:412px">WELCOME TO FERNHOLLOW</h1>
  <p class="welcome-text abs">Fernhollow is Reno's newest, most elegant special events center. Our onsite staff and catering department can assist you in planning the event you desire. From wedding receptions and ceremonies to business meetings or any other special occasion, we offer full service event planning and catering to create a truly unique and memorable experience.</p>
  <a class="btn abs">READ MORE</a>

  <h2 class="section-title abs" style="top:592px">OUR EVENTS</h2>
  <div class="event-photo abs" style="left:52px;background:radial-gradient(ellipse 60px 40px at 87px 35px,#b8a070,transparent 75%),linear-gradient(90deg,#5a3e2e 0%,#c99aa0 20%,#e8d8d0 50%,#c99aa0 80%,#5a3e2e 100%)" role="img" aria-label="Wedding table under a floral arch"></div>
  <div class="event-photo abs" style="left:244px;background:radial-gradient(ellipse 70px 30px at 87px 70px,#f4f2f0,transparent 75%),linear-gradient(180deg,#4a3a30 0%,#a89484 35%,#e2dcd6 70%,#cfc6be 100%)" role="img" aria-label="Banquet hall set with white round tables"></div>
  <div class="event-photo abs" style="left:437px;background:radial-gradient(ellipse 40px 50px at 110px 60px,#a88f78,transparent 75%),linear-gradient(160deg,#3a2618 0%,#b07a48 40%,#d6a46a 65%,#6a4426 100%)" role="img" aria-label="Lounge with stone fireplace"></div>
  <div class="event-photo abs" style="left:630px;background:radial-gradient(ellipse 50px 25px at 50px 55px,#d0602e,transparent 75%),radial-gradient(ellipse 50px 25px at 125px 55px,#d0602e,transparent 75%),linear-gradient(180deg,#4a4038 0%,#8a8070 40%,#b0a898 75%,#8a8278 100%)" role="img" aria-label="Outdoor ceremony seating at dusk"></div>
  <span class="dot abs" style="left:418px;background:#9a9a9a"></span>
  <span class="dot abs" style="left:430px;background:#cfcfcf"></span>

  <h2 class="block-title abs" style="left:52px;top:787px">MENU</h2>
  <div class="rule abs" style="left:52px;top:813px;width:338px"></div>
  <div class="menu-photo abs" style="left:51px;background:radial-gradient(ellipse 35px 28px at 80px 45px,#c0302a,transparent 80%),radial-gradient(ellipse 65px 30px at 80px 60px,#ffffff,transparent 80%),linear-gradient(180deg,#d8d2ce,#ece8e4)" role="img" aria-label="Dessert with strawberries and cream"></div>
  <div class="menu-photo abs" style="left:230px;background:radial-gradient(ellipse 35px 28px at 80px 48px,#6a3a22,transparent 80%),radial-gradient(ellipse 65px 30px at 80px 60px,#d89a40,transparent 80%),linear-gradient(180deg,#cfc8c2,#ece8e4)" role="img" aria-label="Plated grilled entrée"></div>
  <p class="menu-text abs" style="left:54px">If you want to know more about our menu enter here.</p>
  <p class="menu-text abs" style="left:230px">If you want to know more about our menu enter here.</p>

  <h2 class="block-title abs" style="left:437px;top:787px">TESTIMONIALS</h2>
  <div class="rule abs" style="left:437px;top:813px;width:367px"></div>

  <div class="avatar abs" style="left:437px;background:radial-gradient(circle at 50% 45%,#c9a88e,#9a8676 70%)" role="img" aria-label="Guest portrait"></div>
  <p class="quote abs" style="left:437px">If you want to know more about this comment enter here.</p>
  <span class="quote-date abs" style="left:437px">Dec. 15 2014</span>

  <div class="avatar abs" style="left:569px;background:radial-gradient(circle at 50% 45%,#c99a80,#4e5a34 70%)" role="img" aria-label="Guest portrait"></div>
  <p class="quote abs" style="left:569px">If you want to know more about this comment enter here.</p>
  <span class="quote-date abs" style="left:569px">Dec. 15 2014</span>

  <div class="avatar abs" style="left:695px;background:radial-gradient(circle at 50% 45%,#d4b09a,#8a7a6c 70%)" role="img" aria-label="Guest portrait"></div>
  <p class="quote abs" style="left:694px">If you want to know more about this comment enter here.</p>
  <span class="quote-date abs" style="left:694px">Dec. 15 2014</span>

  <footer class="site-footer abs" role="img" aria-label="Brown footer backdrop with faint floral shading"></footer>
  <ul class="footer-col abs" style="left:53px">
    <li>HOME</li><li>ABOUT US</li>
    <li class="sub">ADA BIO</li><li class="sub">NELL BIO</li><li class="sub">ROSE BIO</li><li class="sub">OWEN BIO</li>
    <li>GALLERY</li><li>WEDDINGS</li>
  </ul>
  <ul class="footer-col abs" style="left:181px">
    <li>MEETINGS</li><li>OTHER EVENTS</li><li>CATERING</li><li>MENUS</li>
  </ul>
  <ul class="footer-col abs" style="left:310px">
    <li>FAQs</li><li>TESTIMONIALS</li><li>SCHEDULE AN APPOINTMENT</li>
  </ul>
  <div class="footer-col abs" style="left:526px">CONTACT US</div>
  <div class="field abs" style="left:526px;top:1051px;width:144px;height:12px">Name</div>
  <div class="field abs" style="left:526px;top:1072px;width:144px;height:12px">E-mail</div>
  <div class="field abs" style="left:526px;top:1093px;width:146px;height:47px;border-radius:9px">Comment</div>

  <span class="social abs" style="left:713px;background:#3b5b9c"></span>
  <span class="social abs" style="left:737px;background:#2aa0db"></span>
  <span class="social abs" style="left:760px;background:#f08a1c"></span>
  <span class="social abs" style="left:783px;background:#222"></span>

  <div class="footer-bar abs">Copyright © 2014. Company Name. All Right reserved</div>
</div>
</body>
</html>
```